Objective: Create a visually stunning and compelling PDF brochure that showcases The Orvelle Peak Lodge as the ultimate luxury hunting destination in Kyrgyzstan, specializing in Marco Polo and Ibex hunts. The PDF should evoke a sense of exclusivity, adventure, and the breathtaking beauty of the Tian Shan mountains, ultimately driving bookings.
Target Audience: High-net-worth individuals, discerning hunters seeking exceptional experiences, adventure travelers, and those interested in unique and luxurious wilderness experiences.
Overall Tone & Style: Sophisticated, elegant, and aspirational. Think high-end travel magazines combined with a touch of rugged adventure. Avoid anything that feels generic or overly commercial. The design should reflect the unparalleled nature of the lodge and the hunts offered. (I'm attaching a reference PDF that i like), as well as another instructions file. Drive link for photos: https://files.brankolu.net/share/folders/7KRM42PTbWq0vnzeHJ5sudYA913_c8LxE?mode=view
Another Link: https://files.brankolu.net/share/u/0/folders/5TWEpk-m8rzaqoLc2BnvXwiyeSKdfuGtm

```html
<!DOCTYPE html>
<html lang="en">
<head>
<meta charset="utf-8">
<title>The Orvelle Peak Lodge – Brochure</title>
<link href="https://fonts.googleapis.com/css2?family=Cinzel:wght@400;600&family=Montserrat:wght@400;600;700&display=swap" rel="stylesheet">
<style>
:root{
  --canvas:#8a8a8a;
  --paper:#ffffff;
  --ink:#231f20;
  --dark:#231f20;
  --red:#c0202e;
  --muted:#f1f1f1;
  --text:#333;
}
*{box-sizing:border-box;margin:0;padding:0}
html,body{width:1200px;height:4987px;overflow:hidden;background:var(--canvas)}
body{position:relative;font-family:"Montserrat",sans-serif;color:var(--text)}
.page{position:absolute;left:383px;width:434px;height:613px;background:var(--paper);overflow:hidden}
.abs{position:absolute}
.photo{position:absolute}
.connector{position:absolute;left:552px;top:1486px;width:29px;height:44px;background:var(--paper)}
.on-top{z-index:2}

/* cover */
.cover{top:215px}
.cover .photo{inset:0;background:linear-gradient(180deg,#dfe3e6 0%,#c4c6c4 28%,#a88f72 55%,#7a6250 80%,#5b4d44 100%)}
.brand{position:absolute;left:0;right:0;text-align:center;font-family:"Cinzel",serif;font-weight:600;color:var(--ink)}
.cover .brand-a{top:62px;font-size:11px}
.cover .brand-b{top:122px;font-size:9px}
.cover-title{position:absolute;top:198px;left:0;right:0;text-align:center;font-family:"Cinzel",serif;font-weight:400;color:#3a3533;line-height:1}
.cover-title .l1{font-size:24px}
.cover-title .l2{font-size:32px;margin-top:4px}
.cover-band{position:absolute;left:0;right:0;bottom:0;height:26px;background:var(--dark);color:#fff;font-family:"Cinzel",serif;font-size:11px;text-align:center;line-height:26px}

/* page 2 */
.paradise{top:871px}
.dark-head{position:absolute;left:0;right:0;top:0;background:var(--dark);text-align:center;color:#fff}
.paradise .dark-head{height:87px;padding-top:14px}
.paradise h2{font-family:"Cinzel",serif;font-weight:400;font-size:30px;letter-spacing:1px}
.paradise .sub{color:var(--red);font-size:18px;letter-spacing:1px}
.body-copy{font-size:7.5px;line-height:1.3;color:#222;text-align:justify}

/* page 3 */
.details{top:1533px}
.section-title{font-family:"Cinzel",serif;color:#fff;font-size:32px;text-align:center}
.tag{position:absolute;background:var(--red);color:#fff;font-weight:700;font-size:12px;padding:3px 14px}
.small-copy{font-size:6px;line-height:1.3;color:#222;text-align:justify}
.route{background:var(--muted)}
.route h4{font-size:11px;font-weight:700;color:var(--ink);border-bottom:1px solid #999;padding-bottom:2px}
.route .red{color:var(--red);font-size:9px;margin:4px 0 6px}

/* page 4 */
.pricing{top:2191px}
.pricing h2{position:absolute;top:20px;left:0;right:0;text-align:center;font-family:"Cinzel",serif;font-weight:400;font-size:32px;color:var(--ink)}
.center{position:absolute;left:0;right:0;text-align:center}
.season{display:inline-block;background:var(--red);color:#fff;font-weight:700;font-size:12px;padding:3px 22px}
.red-text{color:var(--red)}
.underlined{display:inline-block;border-bottom:1px solid #555;padding-bottom:2px;font-weight:700;font-size:13px}
.incl{position:absolute;left:30px;right:30px}
.incl h5{font-size:9px;font-weight:700;color:var(--ink);display:inline-block;border-bottom:1px solid #666;padding-bottom:1px;margin-bottom:4px}
.incl ul{list-style:none;font-size:7.5px;line-height:1.6;padding-left:10px}
.incl li::before{content:"•";margin-right:5px}
.price-list{font-size:9.5px;font-weight:700;color:var(--ink);line-height:2}
.addon-band{position:absolute;left:0;right:0;bottom:0;height:91px;background:var(--dark);color:#fff;text-align:center;padding-top:16px;font-size:9.5px;font-weight:700;line-height:1.9}

/* page 5 */
.adventures{top:2849px;background:#1d3660}
.adventures .dark-head{height:62px;padding-top:12px}
.adventures h2{font-family:"Cinzel",serif;font-weight:400;font-size:32px}
.adventures .sub{position:absolute;left:0;right:0;top:68px;text-align:center;color:#fff;font-size:12px;line-height:1.6}
.panel-copy{position:absolute;color:#fff;font-size:12px;line-height:1.5}

/* page 6 */
.lodge{top:3507px;background:#3a2414}
.lodge-title{position:absolute;top:318px;left:0;right:0;text-align:center;font-family:"Cinzel",serif;font-size:38px;color:#fff;font-weight:600}
.lodge-band{position:absolute;top:364px;left:60px;right:60px;height:58px;background:rgba(20,14,10,.85);color:#fff;font-size:7.5px;font-weight:700;text-align:center;line-height:1.3;padding:4px 6px 0}

/* page 7 */
.back{top:4165px;background:var(--dark);color:#fff}
.back .brand{color:#fff}
.contacts{position:absolute;top:555px;left:0;right:0;text-align:center;font-size:8px;line-height:1.5}
.contacts svg{vertical-align:middle;margin-right:3px}
</style>
</head>
<body>

<section class="page cover">
  <div class="photo" role="img" aria-label="Hunter in camouflage seated on a rocky ridge overlooking snow-capped Tian Shan mountains under cloudy sky"></div>
  <div class="brand brand-a">Trailmarke</div>
  <div class="brand brand-b">Veyra Partners</div>
  <h1 class="cover-title"><div class="l1">The Orvelle</div><div class="l2">Peak Lodge</div></h1>
  <div class="cover-band">Kyrgyzstan 2025</div>
</section>

<section class="page paradise">
  <div class="dark-head">
    <h2>A HUNTER'S PARADISE:</h2>
    <div class="sub">Where Luxury Roams Free</div>
  </div>
  <div class="photo" style="left:0;top:91px;width:434px;height:286px;background:linear-gradient(180deg,#9fb2c4 0%,#c8ccd0 30%,#8a7d6e 60%,#5e5650 100%)" role="img" aria-label="Jagged mountain range above a wide gravel valley"></div>
  <p class="abs body-copy" style="left:16px;top:452px;width:245px">Renowned as one of the Best Mountain Hunting Lodges in the World, this Kyrgyzstan camp offers adventure and luxury in the majestic Tian Shan Mountains. Hunt Marco Polo sheep and Ibex across rugged terrain, then relax in unparalleled comfort. Unwind in this secluded oasis, surrounded by breathtaking panoramas of the Kyrgyz landscape. This is where the adventure of the hunt seamlessly blends with the comforts of an unparalleled wilderness retreat.</p>
  <div class="photo" style="left:279px;top:383px;width:155px;height:230px;background:linear-gradient(180deg,#6b3f1c 0%,#b3783d 50%,#4a2a12 100%)" role="img" aria-label="Long timber-lined lodge hallway with warm lighting"></div>
</section>
<div class="connector"></div>

<section class="page details">
  <div class="photo" style="left:0;top:0;width:434px;height:222px;background:linear-gradient(180deg,#3f6fa8 0%,#a9c1d8 35%,#8d7560 65%,#4f4a44 100%)" role="img" aria-label="Mountain valley with braided river under blue sky"></div>
  <div class="abs section-title" style="left:0;right:0;top:180px">HUNT DETAILS</div>
  <div class="tag" style="left:8px;top:224px">HIGHLIGHTS</div>
  <p class="abs small-copy" style="left:14px;top:245px;width:408px">Experience an unforgettable hunting adventure in Kyrgyzstan's majestic Tian Shan Mountains. Pursue the elusive Marco Polo sheep and Siberian Ibex, hunting on horseback alongside seasoned local guides. Sharpen your long-range shooting skills, as accuracy at 400-600 meters may be required. The breathtaking scenery, from towering peaks to vast valleys, provides a stunning backdrop. This unique combination of challenging hunts and unparalleled landscapes creates a truly once-in-a-lifetime experience.</p>
  <div class="tag" style="left:8px;top:313px">PROPERTY FACTS</div>
  <p class="abs small-copy" style="left:14px;top:340px;width:170px">Nestled deep within the majestic Tian Shan mountains, this hunting camp, a unique endeavor by the Kyrgyz government, offers an unparalleled wilderness experience. While the eight luxurious rooms each provide private bathrooms and unexpected amenities like reliable WiFi – a true rarity in such a remote setting – it's the communal spaces that truly capture the grandeur of the surroundings. The lounge area, with its striking floor-to-ceiling windows, frames breathtaking panoramic vistas of the rugged landscape. This blend of modern comforts and unspoiled wilderness creates a hunting retreat unlike any other.</p>
  <div class="abs route" style="left:211px;top:315px;width:223px;height:107px;padding:6px 12px">
    <h4>GETTING THERE</h4>
    <div class="red">Recommended Route</div>
    <p class="small-copy">International flights typically arrive at Manas International Airport (FRU) in Bishkek, Kyrgyzstan, often with layovers in Istanbul or Dubai. Upon arrival, our team will assist with firearms clearance. For guests arriving late, overnight accommodations in Bishkek can be arranged. From Bishkek, hunters have two options to reach the hunting area in the mountains: a 12-hour scenic drive or a 2.5-hour helicopter flight.</p>
  </div>
  <div class="photo" style="left:14px;top:490px;width:406px;height:92px;background:linear-gradient(90deg,#e7e4df 0%,#d9c9ae 55%,#c4a985 100%)" role="img" aria-label="Terrain map of Kyrgyzstan with a pin marking the lodge location"></div>
  <svg class="abs" style="left:230px;top:518px" width="14" height="20" viewBox="0 0 14 20" aria-hidden="true"><path d="M7 0C3 0 0 3 0 7c0 5 7 13 7 13s7-8 7-13c0-4-3-7-7-7z" fill="#d3242c"/><circle cx="7" cy="7" r="2.5" fill="#fff"/></svg>
</section>

<section class="page pricing">
  <h2>DATES &amp; PRICING</h2>
  <div class="center" style="top:83px"><span class="season">SEASON DATES</span></div>
  <div class="center red-text" style="top:108px;font-size:12px;line-height:1.25">August 15th 2025 –<br>November 30th 2025</div>
  <div class="center" style="top:160px"><span class="underlined red-text">INCLUSIONS</span></div>
  <div class="incl" style="top:193px">
    <h5>GUIDED HUNT</h5>
    <ul><li>7-day guided horseback hunt for Marco Polo Argali, Ibex or Both</li><li>Exclusive access to some of the finest hunting areas in Kyrgyzstan</li><li>Trophy Skinning and field preparation</li></ul>
  </div>
  <div class="incl" style="top:270px">
    <h5>FOOD &amp; DRINK</h5>
    <ul><li>Chef-prepared breakfast, packed lunch and dinner</li><li>A selection of non-alcoholic beverages</li></ul>
  </div>
  <div class="incl" style="top:330px">
    <h5>TRAVEL &amp; LOGISTICS</h5>
    <ul><li>Pre-arrival custom planning with the Trailmarke Team</li><li>Round trip, fixed-time airport transfers to Bishkek</li></ul>
  </div>
  <div class="center" style="top:405px"><span class="underlined red-text">PRICING</span></div>
  <div class="center price-list" style="top:436px">MARCO POLO AND IBEX COMBO - $39,500 (min. 2 hunters)<br>MARCO POLO ARGALI - $32,500 (min. 2 hunters)<br>MID-ASIAN IBEX - $10,500 (Min. 2 hunters)</div>
  <div class="addon-band">
    <div class="red-text" style="font-size:13px">POPULAR ADD ONS</div>
    WOLF (Opportunistic): $2,500<br>Extra Ibex $5,500
  </div>
</section>

<section class="page adventures">
  <div class="dark-head">
    <h2>THE ADVENTURES</h2>
  </div>
  <div class="photo" style="left:0;top:62px;width:434px;height:232px;background:linear-gradient(180deg,#1d4e9a 0%,#3f79bd 40%,#7c6a55 70%,#4c3e30 100%)" role="img" aria-label="Timber lodge on a grassy plateau beneath mountains at dusk"></div>
  <div class="sub on-top">A Horseback Ride You'll Never Forget.<br>Challenging Hunts For Prized Game.</div>
  <div class="panel-copy" style="left:16px;top:300px">A Stunning Camp<br>To Revitalize Your Spirit.<br>This Is The Hunt Of A Lifetime.</div>
  <div class="photo" style="left:0;top:397px;width:219px;height:216px;background:linear-gradient(180deg,#6d8bb0 0%,#c5b59f 50%,#8b6a4c 100%)" role="img" aria-label="Hunter posing with a harvested ibex trophy on rocky ground"></div>
  <div class="photo" style="left:219px;top:294px;width:215px;height:151px;background:linear-gradient(180deg,#5d5f62 0%,#8f8c88 60%,#6a645e 100%)" role="img" aria-label="Rider on a white horse climbing a scree slope"></div>
  <div class="photo" style="left:219px;top:445px;width:215px;height:168px;background:linear-gradient(180deg,#2d64b5 0%,#7eaee0 45%,#9a6a3c 75%,#5e3d22 100%)" role="img" aria-label="Wooden guest cabin under a bright blue sky"></div>
</section>

<section class="page lodge">
  <div class="photo" style="left:0;top:0;width:209px;height:170px;background:linear-gradient(180deg,#a86a2e,#6b3d18)" role="img" aria-label="Timber lounge with mounted trophies"></div>
  <div class="photo" style="left:211px;top:0;width:223px;height:130px;background:linear-gradient(180deg,#6a4524,#2f6a6e 60%,#3a2616)" role="img" aria-label="Games room with a billiard table"></div>
  <div class="photo" style="left:0;top:172px;width:209px;height:180px;background:linear-gradient(180deg,#8b5a2e,#c8a882 60%,#5c3a1c)" role="img" aria-label="Living area with white sofas and wooden walls"></div>
  <div class="photo" style="left:211px;top:132px;width:223px;height:220px;background:linear-gradient(180deg,#b47a3c,#7b4c22)" role="img" aria-label="Dining hall with wooden ceiling and artwork"></div>
  <div class="photo" style="left:0;top:354px;width:209px;height:259px;background:linear-gradient(180deg,#5b3a1e,#c08a4c 60%,#4a2c14)" role="img" aria-label="Lit corridor of guest rooms"></div>
  <div class="photo" style="left:211px;top:354px;width:223px;height:259px;background:linear-gradient(180deg,#3b2614,#d29a4e 55%,#3a2414)" role="img" aria-label="Lodge interior at night with warm windows and beams"></div>
  <div class="lodge-title">THE LODGE</div>
  <div class="lodge-band">BEYOND THE REACH OF ORDINARY TRAVEL LIES A HIDDEN WORLD OF SPECTACULAR BEAUTY AND UNRIVALED HUNTING. OUR KYRGYZSTAN EXPERIENCE IS CRAFTED FOR THE DISCERNING SPORTSMAN, OFFERING ACCESS TO PRISTINE WILDERNESS AND LUXURIOUS ACCOMMODATIONS. THIS IS HUNTING ELEVATED TO AN ART FORM.</div>
</section>

<section class="page back">
  <div class="brand" style="top:135px;font-size:14px">Trailmarke</div>
  <div class="brand" style="top:345px;font-size:13px">Veyra Partners</div>
  <div class="contacts">
    <div><svg width="7" height="7" viewBox="0 0 10 10" aria-hidden="true"><path d="M2 0l2 3-1 1a6 6 0 003 3l1-1 3 2-1 2C4 10 0 6 0 1z" fill="#fff"/></svg>+000 555 0192</div>
    <div><svg width="7" height="7" viewBox="0 0 10 10" aria-hidden="true"><circle cx="5" cy="5" r="4.3" fill="none" stroke="#fff"/></svg>www.trailmarke.com</div>
    <div><svg width="8" height="6" viewBox="0 0 10 7" aria-hidden="true"><rect x=".5" y=".5" width="9" height="6" fill="none" stroke="#fff"/><path d="M.5.5L5 4 9.5.5" fill="none" stroke="#fff"/></svg>contact@trailmarke.com</div>
  </div>
</section>

</body>
</html>
```